Denim Retailer needs advert for sale

We need a advertisement designed that can be used to market our upcoming promotion through our electronic media channels which include Facebook, email & website.

Promotion Details:

Title: Pick A Pair Sale
Offer: Buy 1 pair =10% off, Buy 2 pairs = 15% off, Buy 3+ pairs = 20% off.

Our main brands are Tavon's, Gallop by Orn & Cobbleton for both men and women.

Our Target market is 25-55 yo male & female.

I would ideally like an eye catching design that encapsulates premise of our promotion. I don't have any specific theme or colour scheme, bust must be gender neutral.

Target Market(s)

25-55 male & female

Industry/Entity Type

Electronic

Requirements
Must have
• Must be sized to accommodate a Facebook post.

```html
<!DOCTYPE html>
<html lang="en">
<head>
<meta charset="utf-8">
<title>Pick A Pair Sale</title>
<link href="https://fonts.googleapis.com/css2?family=Abril+Fatface&family=Playfair+Display:wght@400;700&family=Questrial&display=swap" rel="stylesheet">
<style>
  :root {
    --stone-dark: #4f4f4f;
    --stone-light: #8a8a8a;
    --plaster: #dcdcdc;
    --plaster-edge: #c4c4c4;
    --band: #050505;
    --ink: #111111;
    --white: #ffffff;
    --mint: #a6ecd2;
    --slate: #24242c;
    --denim: #6b8db6;
    --sand: #d9d5ca;
    --pink: #e2357a;
    --grey-text: #8c8c8c;
    --dark-denim: #1c2234;
    --light-denim: #8fb1cf;
  }
  * { margin: 0; padding: 0; box-sizing: border-box; }
  html, body { width: 1114px; height: 1200px; overflow: hidden; background: var(--plaster); }
  .advert { position: relative; width: 1114px; height: 1200px; overflow: hidden; font-family: "Questrial", sans-serif; }

  .backdrop-top { position: absolute; left: 0; top: 0; width: 1114px; height: 416px;
    background: radial-gradient(ellipse at 35% 30%, var(--stone-light), var(--stone-dark) 75%); }
  .backdrop-bottom { position: absolute; left: 0; top: 416px; width: 1114px; height: 784px;
    background: radial-gradient(ellipse at 50% 40%, #ececec, var(--plaster-edge) 85%); }
  .band { position: absolute; left: 0; top: 703px; width: 1114px; height: 133px; background: var(--band); }

  .model { position: absolute; }
  .model-women { left: 0; top: 428px; width: 318px; height: 772px;
    background: linear-gradient(180deg, var(--dark-denim) 0%, #27304a 70%, #2c49b8 92%, #b07a45 100%); }
  .model-men { left: 703px; top: 386px; width: 378px; height: 814px;
    background: linear-gradient(180deg, #c9a58e 0%, var(--light-denim) 12%, #a8c4dc 60%, #7e97b3 88%, #3d4660 100%); }

  .links { position: absolute; left: 34px; top: 78px; color: var(--white); font-family: Arial, sans-serif; font-size: 20px; line-height: 28px; }

  .title { position: absolute; right: 22px; top: 34px; text-align: right; font-family: "Abril Fatface", serif; font-weight: 400; line-height: 1; }
  .title-top { display: block; font-size: 96px; letter-spacing: -1px; }
  .title-top .dark { color: var(--ink); -webkit-text-stroke: 2px var(--white); text-shadow: 3px 4px 6px rgba(0,0,0,.5); }
  .title-top .mint, .title-sale { color: var(--mint); text-shadow: 3px 4px 6px rgba(0,0,0,.45); }
  .title-sale { display: block; font-family: "Playfair Display", serif; font-weight: 400; font-size: 200px; margin-top: -6px; }

  .offer-panel { position: absolute; left: 322px; top: 206px; width: 384px; height: 856px; background: var(--white);
    box-shadow: 0 0 18px rgba(0,0,0,.35); }
  .offer { position: absolute; left: 16px; width: 356px; height: 218px; color: var(--white); text-align: center;
    font-size: 68px; line-height: 1.05; padding-top: 38px; }
  .offer-one { top: 17px; background: var(--slate); }
  .offer-two { top: 253px; background: var(--denim); }
  .offer-three { top: 488px; background: var(--sand); text-shadow: 0 0 2px #333, 2px 3px 3px #333; }
  .buy-tag { position: absolute; left: -8px; top: 4px; background: var(--pink); color: #1a1a1a; font-size: 22px;
    padding: 2px 8px; transform: rotate(-22deg); border: 2px solid #2a2a2a; text-shadow: none; }

  .brand-strip { position: absolute; left: 16px; top: 724px; width: 356px; height: 116px; background: var(--slate);
    display: flex; align-items: center; justify-content: center; }
  .brand-name { color: var(--white); font-size: 44px; }

  .audience { position: absolute; left: 749px; top: 722px; font-family: "Playfair Display", serif; line-height: 1; }
  .audience .muted { color: var(--grey-text); font-size: 42px; }
  .audience .accent { color: var(--denim); font-size: 60px; }
  .audience-line2 { display: block; margin-left: 40px; }
</style>
</head>
<body>
<div class="advert">
  <div class="backdrop-top" role="img" aria-label="Grey concrete wall texture"></div>
  <div class="backdrop-bottom" role="img" aria-label="Pale cracked plaster texture"></div>
  <div class="band"></div>

  <div class="model model-women" role="img" aria-label="Woman in dark skinny jeans and blue heels, waist down"></div>
  <div class="model model-men" role="img" aria-label="Man in light blue jeans and navy sneakers, waist down"></div>

  <div class="links">
    <p>www.friendwall.net/yourpage</p>
    <p>www.pickapairjeans.com</p>
  </div>

  <h1 class="title">
    <span class="title-top"><span class="dark">Pick A </span><span class="mint">Pair</span></span>
    <span class="title-sale">Sale</span>
  </h1>

  <div class="offer-panel">
    <div class="offer offer-one"><span class="buy-tag">BUY</span>1 pair<br>10% off</div>
    <div class="offer offer-two"><span class="buy-tag">BUY</span>2 pairs<br>15% off</div>
    <div class="offer offer-three"><span class="buy-tag">BUY</span>3+ pairs<br>20% off</div>
    <div class="brand-strip">
      <span class="brand-name">Gallop by Orn</span>
    </div>
  </div>

  <p class="audience">
    <span class="muted">for </span><span class="accent">men</span>
    <span class="audience-line2"><span class="muted">and </span><span class="accent">women</span></span>
  </p>
</div>
</body>
</html>
```